Rising Harbor Glow Gala Graphic Design

I’m seeking a professional graphic designer experienced in event branding to create a cohesive suite of materials for our third annual fundraising gala, “Rising Harbor Glow.” This year's theme is " An Evening in Silver for Rising Harbor Glow" Need to design collateral for website, social media and email blasts.
Target Market(s)
Affluent gala attendees
Industry/Entity Type
Fundraising / Charity / Outdoors / Sports
Font styles to use
Decorative
Script
Colors
0054AA
0677BA
7BADD7
CADEEF
E8F1F8
0094D4
00A9DD
6FCCEA
C7EBF8
E9F6FB
00AB8E
00BBA5
67D7C9
C6EFE9
E9F9F6
6B429C
8869AF
B7A5CE
E3DAEB
F3F0F8

```html
<!DOCTYPE html>
<html lang="en">
<head>
<meta charset="utf-8">
<title>Rising Harbor Glow — Gala</title>
<link rel="stylesheet" href="https://fonts.googleapis.com/css2?family=Cinzel+Decorative:wght@700&family=Cormorant+Garamond:wght@300&family=Italiana&family=Pinyon+Script&display=swap">
<style>
  :root {
    --harbor-night: #06122b;
    --deep-blue: #0054aa;
    --ocean-blue: #0677ba;
    --sky-blue: #0094d4;
    --bright-aqua: #6fccea;
    --teal: #00bba5;
    --violet: #6b429c;
    --lilac: #8869af;
    --silver-white: #f3f0f8;
    --silver: #c9d2dc;
    --body-silver: #a9b6c6;
  }
  html, body {
    margin: 0;
    padding: 0;
    overflow: hidden;
    background: var(--harbor-night);
  }
  .gala-poster {
    position: relative;
    width: 1157px;
    height: 1200px;
    overflow: hidden;
    background: var(--harbor-night);
  }
  .sparkler-photo {
    position: absolute;
    inset: 0;
    background:
      radial-gradient(ellipse 210px 160px at 270px 530px, rgba(111, 204, 234, 0.55), transparent 70%),
      radial-gradient(ellipse 430px 340px at 290px 520px, rgba(0, 148, 212, 0.35), transparent 75%),
      radial-gradient(ellipse 130px 100px at 725px 275px, rgba(0, 187, 165, 0.35), transparent 70%),
      radial-gradient(ellipse 240px 340px at 790px 800px, rgba(136, 105, 175, 0.35), transparent 75%),
      radial-gradient(ellipse 300px 200px at 980px 1080px, rgba(107, 66, 156, 0.3), transparent 75%),
      linear-gradient(160deg, #0a1d45 0%, var(--harbor-night) 55%, #140d2c 100%);
  }
  .brand-mark {
    position: absolute;
    left: 510px;
    top: 346px;
    width: 136px;
    height: 162px;
  }
  .event-title {
    margin: 0;
    font-weight: normal;
    color: var(--silver-white);
  }
  .event-title span {
    position: absolute;
    left: 0;
    right: 0;
    text-align: center;
    line-height: 1;
    white-space: nowrap;
  }
  .event-title__lead {
    top: 522px;
    font-family: "Cinzel Decorative", serif;
    font-weight: 700;
    font-size: 70px;
    letter-spacing: 4px;
    color: var(--silver);
  }
  .event-title__middle {
    top: 588px;
    font-family: "Pinyon Script", cursive;
    font-size: 100px;
    color: var(--silver-white);
  }
  .event-title__main {
    top: 666px;
    font-family: "Cormorant Garamond", serif;
    font-weight: 300;
    font-size: 192px;
    color: var(--silver-white);
  }
  .event-intro {
    position: absolute;
    left: 150px;
    width: 857px;
    top: 913px;
    margin: 0;
    text-align: center;
    font-family: "Italiana", serif;
    font-size: 32px;
    line-height: 40px;
    color: var(--body-silver);
  }
  .event-intro span {
    display: block;
    white-space: nowrap;
  }
</style>
</head>
<body>
  <main class="gala-poster">
    <div class="sparkler-photo" role="img" aria-label="Close-up photograph of a lit sparkler throwing glowing sparks against a dark night sky, toned in harbor blues, teal and violet"></div>

    <svg class="brand-mark" viewBox="0 0 136 162" aria-hidden="true">
      <circle cx="68" cy="81" r="64" fill="var(--silver-white)"/>
    </svg>

    <h1 class="event-title">
      <span class="event-title__lead">RISING</span>
      <span class="event-title__middle">harbor</span>
      <span class="event-title__main">Glow</span>
    </h1>

    <p class="event-intro">
      <span>Lorem ipsum dolor sit amet, consectetuer adipiscing</span>
      <span>elit, sed diam nonummy nibh euismod tincidunt ut</span>
      <span>laoreet dolore magna aliquam erat volutpat. Ut wisi</span>
      <span>enim ad</span>
    </p>
  </main>
</body>
</html>
```